Pale Lantern Double Sided Flyer Design

We need a double sided flyer (1/3 of an A4 which is 99mm x 210mm) developed for our Newcastle(NSW) tour. This flyer will be placed in tourist information centres and hotels. We want it to direct people to our website or be able to make bookings over the phone.

About Us:-
We are a city walking tour company that runs tours day or night. We run both day and night and will incorporate real history / real Pale lantern. Some of the stories will be quite serious i.e.- there are infamous murders from 100 years ago, baffling court cases, even a bit of poetry written by murderers, suicides, love triangles, you name it. We will be telling the historical stories that tourists will not hear from any other tour provider. A bit of darkness, a bit of mystery and a bit of history theme.

We do no go for scares and let the very real stories deliver the entertainment for our guests. Our customers enjoy our tours, but it isn't light fun and frivolity. Our stories are being carefully crafted and are packed with unexpected twists, turns; revelations whilst remaining all 100% true. We deliver deep, rich, engaging stories.

Here are a few samples of quotes from the characters in our stories that may give you an idea of the kind of history we will cover:-

"There were bits of spines, bits of skulls, [and] finger bones spilled out all over the streets - I ended up filling three boxes. Children were playing with them for weeks”

"I had a close shave last night and now I want a close haircut.”

“She's a beautiful child', isn't she? She's the cause of all the trouble.”

“I did it because she would not come home with me.”

"I have killed my wife. I’m glad she’s dead.”

"Stand aside or I'll put a bullet through both of you."

“You villain, I'll teach you to take away my character."

“You’re not dead yet, you bastard!”

Our website, booking form and contact details can be viewed at www.palelantern.com.au

Target Market(s)

Tourists

Industry/Entity Type

Tour

Colors

Designer to choose colors to be used in the design.

Requirements
Must have
• Vertical orientation please.
• Please also include a reference to a discount offer of 25% using the promo code "WICK".
Nice to have
• FRONT FLYER INFORMATION
• - Pale Lantern Logo
• - "I have killed my wife; I'm glad she's dead."
• - Harbourside Hidden Lanes Walk
• - 25% Discount Offer Codeword WICK
• - web address at the base; www.palelantern.com.au
• BACK FLYER INFORMATION
• - "She's a beautiful child', isn't she? She's the cause of all the trouble.
• - Pale Lantern Logo at the base along with the web address www.palelantern.com.au
• - Blurb:- Pale lantern brings back Newcastle's hidden past, the forgotten past, the dark past that may not want to be remembered.
• Real stories from the streets around you. Discover the histories you won't hear anywhere else. The forgotten stories of yesteryear finally get a chance to be told. Through you they get to live again.
Should not have
• GENERAL
• Please do not include the phone number, email address or social media icons. We want to drive online bookings.

```html
<!DOCTYPE html>
<html lang="en">
<head>
<meta charset="utf-8">
<title>Pale Lantern – Harbourside Hidden Lanes Walk Flyer</title>
<link rel="stylesheet" href="https://fonts.googleapis.com/css2?family=Lato:wght@400;700&family=Creepster&display=swap">
<style>
  :root {
    --stage: #d8d3ce;
    --flyer-black: #141414;
    --flyer-charcoal: #242626;
    --blood: #e01e1e;
    --blood-deep: #b5141a;
    --ink-white: #ffffff;
    --text-font: "Lato", Arial, sans-serif;
    --drip-font: "Creepster", "Lato", cursive;
  }
  * { box-sizing: border-box; margin: 0; padding: 0; }
  html, body {
    width: 1200px; height: 1200px; overflow: hidden;
    background: var(--stage);
  }
  .canvas { position: relative; width: 1200px; height: 1200px; }

  .flyer {
    position: absolute;
    overflow: hidden;
    background: radial-gradient(ellipse at 50% 40%, var(--flyer-charcoal), var(--flyer-black) 75%);
    color: var(--ink-white);
    font-family: var(--text-font);
    text-align: center;
  }
  .flyer--front { left: 122px; top: 134px; width: 466px; height: 954px; }
  .flyer--back  { left: 642px; top: 134px; width: 462px; height: 946px; }

  .line { position: absolute; left: 0; right: 0; line-height: 1; white-space: nowrap; }

  .street-photo {
    position: absolute; inset: 0 0 200px 0;
    background: linear-gradient(160deg, #2e3232 0%, #3c4242 35%, #1e2020 70%, transparent 100%);
    opacity: .85;
  }

  .blood-splash {
    position: absolute; border-radius: 50%;
    background: radial-gradient(circle, var(--blood) 0%, var(--blood) 55%, var(--blood-deep) 68%, rgba(181,20,26,0) 80%);
  }
  .flyer--front .blood-splash { left: 30px; top: 250px; width: 420px; height: 440px; }
  .flyer--back  .blood-splash { left: 90px; top: 400px; width: 300px; height: 290px; }

  .brand { font-weight: 700; letter-spacing: .5px; }
  .flyer--front .brand { top: 304px; font-size: 38px; }
  .flyer--back .brand  { top: 128px; font-size: 32px; }

  .quote { font-weight: 700; font-size: 35px; }
  .quote--drip { font-family: var(--drip-font); font-weight: 400; font-size: 66px; }
  .q1 { top: 340px; }
  .q2 { top: 508px - 0px; }

  .web { font-weight: 700; }
  .flyer--front .web { top: 851px; font-size: 29px; }
  .flyer--back .web  { top: 863px; font-size: 30px; color: var(--blood); }

  .offer-lead { top: 174px; font-weight: 700; font-size: 32px; }
  .offer-amount { top: 200px; font-weight: 700; font-size: 186px; color: var(--blood); letter-spacing: -4px; }
  .offer-code-lead { top: 375px; font-weight: 700; font-size: 29px; }
  .promo-code { top: 500px; font-family: var(--drip-font); font-size: 74px; }

  .contact-note { top: 772px; font-weight: 700; font-size: 20px; line-height: 1.2; white-space: normal; }
</style>
</head>
<body>
<main class="canvas">

  <section class="flyer flyer--front" aria-label="Flyer front">
    <div class="street-photo" role="img" aria-label="Dark photograph of a historic sandstone street"></div>
    <div class="blood-splash" role="img" aria-label="Red blood splatter"></div>
    <p class="line brand">PALE LANTERN</p>
    <p class="line quote" style="top:342px">I HAVE</p>
    <p class="line quote quote--drip" style="top:384px">KILLED</p>
    <p class="line quote" style="top:458px">MY WIFE</p>
    <p class="line quote" style="top:498px">I’M GLAD SHE’S</p>
    <p class="line quote quote--drip" style="top:540px">DEAD</p>
    <p class="line web">www.palelantern.com.au</p>
  </section>

  <section class="flyer flyer--back" aria-label="Flyer back">
    <div class="blood-splash" role="img" aria-label="Red blood splatter"></div>
    <p class="line brand">PALE LANTERN</p>
    <p class="line offer-lead">DISCOUNT OFFER OF</p>
    <p class="line offer-amount">25%</p>
    <p class="line offer-code-lead">USING THE PROMO CODE</p>
    <p class="line promo-code">WICK</p>
    <p class="line contact-note">OUR WEBSITE, BOOKING<br>FORM AND CONTACT DETAILS<br>CAN BE VIEWED AT</p>
    <p class="line web">www.palelantern.com.au</p>
  </section>

</main>
</body>
</html>
```